DLW Flyer 2022

Need a flyer/Brochure it it an information piece on or company to give to clients during Sales call. I have started something in Canva but would like it more professional designed. We we are a Fire & Security company.
we do alot of cloud based systems. New system intercoms, Camera systems, Card Access and fire alarm systems

```html
<!DOCTYPE html>
<html lang="en">
<head>
<meta charset="utf-8">
<title>DLW Fire &amp; Security Brochure</title>
<link href="https://fonts.googleapis.com/css2?family=Montserrat:wght@400;500;600;700;800&family=Oswald:wght@700&display=swap" rel="stylesheet">
<style>
:root{
  --red:#d42027;
  --red-deep:#b3161d;
  --dark:#2a2a2c;
  --ink:#1f1f21;
  --paper:#ffffff;
  --mist:#eef0f2;
  --stage:#e6e7e9;
  --blue-1:#0b2f63;
  --blue-2:#1f63b0;
  --blue-3:#5fb4ea;
}
*{box-sizing:border-box;margin:0;padding:0}
html,body{width:1200px;height:1200px;overflow:hidden;background:var(--stage);font-family:"Montserrat",sans-serif;color:var(--ink)}
.spread{position:absolute;left:220px;width:760px;height:575px;display:grid;grid-template-columns:repeat(3,1fr);background:var(--paper);box-shadow:0 6px 18px rgba(0,0,0,.18)}
.spread--outside{top:14px}
.spread--inside{top:611px}
.panel{position:relative;overflow:hidden;border-right:1px solid #e2e2e2}
.panel:last-child{border-right:none}
.abs{position:absolute}
.red{color:var(--red)}
.brand{display:flex;align-items:center;gap:6px;font-weight:800;color:var(--red);letter-spacing:1px}
.brand__dot{width:10px;height:10px;background:var(--red);border-radius:50%}

/* About panel */
.about__intro{left:18px;top:22px;right:18px}
.about__title{font-size:16px;font-weight:800;margin-bottom:6px}
.about__lead{font-size:9.5px;font-weight:600;line-height:1.4}
.about__box{left:0;top:112px;width:100%;height:296px;background:var(--red);color:#fff;padding:16px 18px;font-size:8.2px;line-height:1.45;font-weight:500}
.about__box p{margin-bottom:9px;text-align:justify}
.about__base{left:0;top:408px;width:100%;height:167px;background:var(--dark)}
.about__devices{left:22px;top:418px;width:212px;height:146px;background:linear-gradient(135deg,#f4f5f7,#b9bec5 60%,#7c838c);border-radius:3px}

/* Trust panel */
.trust__head{left:18px;top:22px;right:14px;font-size:10.5px;font-weight:700;line-height:1.3}
.trust__box{left:0;top:92px;width:100%;height:240px;background:var(--red);color:#fff;padding:14px 22px;text-align:center}
.trust__mark{font-family:"Oswald",sans-serif;font-size:34px;line-height:.8;text-align:left;color:#f5c9cb}
.trust__quote{font-size:10.2px;font-weight:600;line-height:1.42;margin-top:2px}
.trust__by{font-size:10px;font-weight:600;margin-top:10px}
.trust__brand{left:40px;top:362px;font-size:34px}
.contact{left:34px;top:420px;list-style:none;font-size:9px;font-weight:500;line-height:1.3}
.contact li{display:flex;align-items:flex-start;gap:7px;margin-bottom:6px}
.contact svg{flex:none;width:14px;height:14px}

/* Cover panel */
.cover__brand{right:22px;top:20px;font-size:30px}
.cover__photo{left:0;top:66px;width:100%;height:270px;background:radial-gradient(circle at 55% 45%,var(--blue-3),var(--blue-2) 35%,var(--blue-1) 85%)}
.cover__banner{left:0;top:312px;width:100%;height:110px;background:var(--red);display:flex;align-items:center;justify-content:center;box-shadow:0 4px 8px rgba(0,0,0,.25)}
.cover__title{font-family:"Oswald",sans-serif;font-size:33px;line-height:1.08;color:#fff;text-align:center;letter-spacing:.5px}
.cover__band{left:0;top:422px;width:100%;height:78px;background:var(--dark);display:flex;align-items:center;justify-content:center;color:#fff;font-size:12px;font-weight:600}
.cover__rule{left:16px;right:16px;top:512px;height:2px;background:var(--red)}

/* Fire panel */
.fire{background:linear-gradient(180deg,var(--mist),#fff)}
.fire__title{left:18px;top:22px;right:16px;font-size:13px;font-weight:600;line-height:1.3}
.fire__photo{left:0;top:72px;width:100%;height:268px;background:linear-gradient(160deg,#d7dbe0,#8c98a6 55%,#3f6fa8)}
.fire__why{left:0;top:326px;width:100%;height:104px;background:var(--red);color:#fff;padding:14px 18px;font-size:8.4px;line-height:1.35}
.fire__why h3{font-size:12px;font-weight:800;margin-bottom:1px}
.fire__why h4{font-size:9.5px;font-weight:700;margin-top:8px}
.fire__quote{left:18px;top:442px;right:16px;font-size:8.6px;line-height:1.4}
.fire__quote h3{color:var(--red);font-size:12px;font-weight:800;margin-bottom:4px}
.fire__quote cite{display:block;font-style:normal;margin-top:6px}

/* Services panel */
.services__strip{left:0;top:0;width:9px;height:520px;background:var(--red)}
.services__tab{left:18px;top:20px;width:170px;height:32px;background:var(--red);color:#fff;font-size:14px;font-weight:800;display:flex;align-items:center;padding-left:12px;box-shadow:4px 4px 0 var(--dark)}
.service-list{left:18px;top:68px;right:12px;list-style:none}
.service{display:flex;gap:9px;align-items:center;height:71px}
.service__icon{flex:none;width:40px;height:40px}
.service h3{color:var(--red);font-size:10px;font-weight:700}
.service p{font-size:8px;line-height:1.3}
.services__base{left:0;top:520px;width:100%;height:55px;background:var(--dark)}

/* Full service panel */
.full__lead{left:16px;top:22px;right:14px;color:var(--red);font-size:10.5px;font-weight:700;line-height:1.3}
.full__body{left:16px;top:84px;right:14px;font-size:8.4px;line-height:1.4}
.full__body h3{font-size:10px;font-weight:700;margin-bottom:1px}
.ticks{display:grid;grid-template-columns:1fr 1fr;list-style:none;margin:7px 0 12px}
.ticks li{display:flex;align-items:center;gap:5px;margin-bottom:3px}
.ticks li::before{content:"";width:7px;height:7px;border-radius:50%;background:var(--red);flex:none}
.full__brand{left:40px;top:294px;font-size:26px}
.full__call{left:40px;top:332px;color:var(--red);font-size:12px;font-weight:800;line-height:1.25}
.full__call span{display:flex;align-items:center;gap:5px;color:var(--ink);font-size:11px;font-weight:700}
.full__products{left:0;top:380px;width:100%;height:195px;background:linear-gradient(180deg,#7fc0e6,#d9dde2 45%,#3a3a3d)}
</style>
</head>
<body>

<section class="spread spread--outside">
  <div class="panel about">
    <div class="abs about__intro">
      <h2 class="about__title">ABOUT <span class="red">US</span></h2>
      <p class="about__lead">Since 1988, DLW has been servicing the Greater Boston and surrounding areas with fire and security systems.</p>
    </div>
    <div class="abs about__box">
      <p>Our Company strives to build lasting relationships; our focus is not on growing but getting better. Many of the people that come to us have had problems with their past company or have a problem that has eluded them. We take the time to identify the problems they face, rectify them, and put them on a service program that fits their needs.</p>
      <p>All our technicians are licensed in the state of Massachusetts and go through many hours of factory and in house training. We all have security safety clearances issued by the state and we are a nationally certified fire alarm service provider. We are also proud members of the national and state fire alarm associations.</p>
      <p>As systems integrators, DLW takes many different systems and combines them to fill our customer's needs.</p>
    </div>
    <div class="abs about__base"></div>
    <div class="abs about__devices" role="img" aria-label="Photo of video intercom door stations and indoor touchscreen monitor"></div>
  </div>

  <div class="panel trust">
    <h2 class="abs trust__head">We're not just in <span class="red">THE BUSINESS OF SECURITY,</span> we're in the business <span class="red">OF TRUST.</span></h2>
    <blockquote class="abs trust__box">
      <div class="trust__mark">&ldquo;</div>
      <p class="trust__quote">I just wanted to say that Ive been really pleased with how responsive DLW has been and how smooth the intercom installation went. Given how old the wiring is in this building, I expected that this would have been harder to do.</p>
      <p class="trust__by">-- Laura Brandt</p>
    </blockquote>
    <div class="abs brand trust__brand"><span class="brand__dot"></span>DLW</div>
    <ul class="abs contact">
      <li><svg viewBox="0 0 14 14"><circle cx="7" cy="7" r="7" fill="#d42027"/><path d="M7 3a2.4 2.4 0 0 0-2.4 2.4C4.6 7.2 7 10.5 7 10.5s2.4-3.3 2.4-5.1A2.4 2.4 0 0 0 7 3zm0 3.3a.9.9 0 1 1 0-1.8.9.9 0 0 1 0 1.8z" fill="#fff"/></svg><span>PO Box 4170<br>Millbrook, MA 01999</span></li>
      <li><svg viewBox="0 0 14 14"><circle cx="7" cy="7" r="7" fill="#d42027"/><path d="M4.6 3.6l1.3-.2.7 1.8-.8.6a5 5 0 0 0 2.4 2.4l.6-.8 1.8.7-.2 1.3c-3.2.3-6.1-2.6-5.8-5.8z" fill="#fff"/></svg><span>(555) 014-2290</span></li>
      <li><svg viewBox="0 0 14 14"><circle cx="7" cy="7" r="7" fill="#d42027"/><rect x="3.5" y="4.5" width="7" height="5" fill="#fff"/><path d="M3.5 4.5 7 7.3l3.5-2.8" stroke="#d42027" stroke-width=".8" fill="none"/></svg><span>sales@dlwsecurity.example</span></li>
      <li><svg viewBox="0 0 14 14"><circle cx="7" cy="7" r="7" fill="#d42027"/><circle cx="7" cy="7" r="3.6" stroke="#fff" stroke-width=".9" fill="none"/><path d="M3.4 7h7.2M7 3.4c-1.6 2.2-1.6 5 0 7.2M7 3.4c1.6 2.2 1.6 5 0 7.2" stroke="#fff" stroke-width=".8" fill="none"/></svg><span>www.dlwsecurity.example</span></li>
    </ul>
  </div>

  <div class="panel cover">
    <div class="abs brand cover__brand"><span class="brand__dot"></span>DLW</div>
    <div class="abs cover__photo" role="img" aria-label="Photo of a businessman touching a glowing digital padlock on a blue security interface"></div>
    <div class="abs cover__banner"><h1 class="cover__title">UNLOCKING<br>THE FUTURE</h1></div>
    <div class="abs cover__band">www.dlwsecurity.example</div>
    <div class="abs cover__rule"></div>
  </div>
</section>

<section class="spread spread--inside">
  <div class="panel fire">
    <h2 class="abs fire__title">Fire Alarm and Emergency Communications Systems</h2>
    <div class="abs fire__photo" role="img" aria-label="Photo of a technician using the microphone of a fire alarm emergency communications panel"></div>
    <div class="abs fire__why">
      <h3>WHY CHOOSE US?</h3>
      <p>We are here to make your job easier.</p>
      <h4>Anonymous</h4>
      <p>Man with hole in pocket feel cocky all day</p>
    </div>
    <div class="abs fire__quote">
      <h3>CLIENT TESTIMONIAL</h3>
      <p>I love using DLW because you always get things done fast and correct for me. As a very busy property manager, it is one less thing for me to worry about knowing you will always get done what I ask you to do.</p>
      <cite>Neil Porter, CMCA<br>Sr. Property Manager |<br>Harbor Lane Properties, LLC</cite>
    </div>
  </div>

  <div class="panel services">
    <div class="abs services__strip"></div>
    <h2 class="abs services__tab">OUR SERVICES</h2>
    <ul class="abs service-list">
      <li class="service">
        <svg class="service__icon" viewBox="0 0 40 40"><circle cx="20" cy="20" r="19" fill="#d42027"/><circle cx="20" cy="20" r="14" fill="none" stroke="#fff" stroke-width="1.2"/><path d="M14 24h12l-2-3v-4a4 4 0 0 0-8 0v4z" fill="none" stroke="#fff" stroke-width="1.4"/><path d="M18.5 26h3" stroke="#fff" stroke-width="1.4"/></svg>
        <div><h3>Fire Alarm</h3><p>We have been installing, servicing, &amp; testing fire alarms for 30 years.</p></div>
      </li>
      <li class="service">
        <svg class="service__icon" viewBox="0 0 40 40"><circle cx="20" cy="20" r="19" fill="#d42027"/><circle cx="20" cy="20" r="14" fill="none" stroke="#fff" stroke-width="1.2"/><rect x="13" y="13" width="14" height="14" rx="1.5" fill="none" stroke="#fff" stroke-width="1.4"/><rect x="15.5" y="15.5" width="9" height="5" fill="none" stroke="#fff" stroke-width="1"/><path d="M16 23.5h2M19 23.5h2M22 23.5h2" stroke="#fff" stroke-width="1.2"/></svg>
        <div><h3>Intercom</h3><p>We have the intercom systems that will meet your requirements.</p></div>
      </li>
      <li class="service">
        <svg class="service__icon" viewBox="0 0 40 40"><circle cx="20" cy="20" r="19" fill="#d42027"/><circle cx="20" cy="20" r="14" fill="none" stroke="#fff" stroke-width="1.2"/><path d="M20 12l7 3v5c0 4-3 7-7 8-4-1-7-4-7-8v-5z" fill="none" stroke="#fff" stroke-width="1.4"/><path d="M17 20l2.2 2.2L23.5 18" fill="none" stroke="#fff" stroke-width="1.4"/></svg>
        <div><h3>Security Systems</h3><p>Professionally installed, serviced and monitored Security Systems provide 24 hour reliable protection for you and your loved one.</p></div>
      </li>
      <li class="service">
        <svg class="service__icon" viewBox="0 0 40 40"><circle cx="20" cy="20" r="19" fill="#d42027"/><circle cx="20" cy="20" r="14" fill="none" stroke="#fff" stroke-width="1.2"/><rect x="12" y="16" width="12" height="8" rx="1" fill="none" stroke="#fff" stroke-width="1.4"/><path d="M24 18.5l4-2v7l-4-2z" fill="none" stroke="#fff" stroke-width="1.4"/></svg>
        <div><h3>Camera Systems</h3><p>We have years of surveillance camera expertise and it shows.</p></div>
      </li>
      <li class="service">
        <svg class="service__icon" viewBox="0 0 40 40"><circle cx="20" cy="20" r="19" fill="#d42027"/><circle cx="20" cy="20" r="14" fill="none" stroke="#fff" stroke-width="1.2"/><path d="M15 13l2.5-.4 1.3 3.4-1.5 1.1a9 9 0 0 0 4.6 4.6l1.1-1.5 3.4 1.3-.4 2.5C20 24.5 14.5 19 15 13z" fill="none" stroke="#fff" stroke-width="1.4"/></svg>
        <div><h3>Telephone Entry</h3><p>Sleep soundly knowing that a monitored wireless security system protects your loved ones and your home.</p></div>
      </li>
      <li class="service">
        <svg class="service__icon" viewBox="0 0 40 40"><circle cx="20" cy="20" r="19" fill="#d42027"/><circle cx="20" cy="20" r="14" fill="none" stroke="#fff" stroke-width="1.2"/><rect x="12" y="15" width="16" height="11" rx="1.5" fill="none" stroke="#fff" stroke-width="1.4"/><path d="M12 18.5h16" stroke="#fff" stroke-width="1.6"/><path d="M15 23h5" stroke="#fff" stroke-width="1.2"/></svg>
        <div><h3>Card Access</h3><p>Combining Access, Cameras and Intercom system to give you complete building management is what we do.</p></div>
      </li>
    </ul>
    <div class="abs services__base"></div>
  </div>

  <div class="panel full">
    <p class="abs full__lead">We take you from system design, to installation to long-term support. And everywhere in between.</p>
    <div class="abs full__body">
      <h3>We are a full-service company.</h3>
      <p>Whether you're starting from scratch, have an old system in dire need of an update, or just want to add something in, we can help.</p>
      <ul class="ticks">
        <li>System Design</li><li>Testing</li>
        <li>Installation</li><li>Maintenance</li>
        <li>Integration</li><li>Monitoring</li>
        <li>Upgrading</li><li>Certified Testing</li>
      </ul>
      <h3>We take pride in our work.</h3>
      <p>Our technicians are trained, experienced, and licensed. We create great results that you can rely on as we strive to build lasting relationships with our clients.</p>
    </div>
    <div class="abs brand full__brand"><span class="brand__dot"></span>DLW</div>
    <div class="abs full__call">CALL US TODAY
      <span><svg width="11" height="11" viewBox="0 0 14 14"><circle cx="7" cy="7" r="7" fill="#d42027"/><path d="M4.6 3.6l1.3-.2.7 1.8-.8.6a5 5 0 0 0 2.4 2.4l.6-.8 1.8.7-.2 1.3c-3.2.3-6.1-2.6-5.8-5.8z" fill="#fff"/></svg>(555) 014-2290</span>
    </div>
    <div class="abs full__products" role="img" aria-label="Photo of security cameras, access readers, a smart lock and monitors in front of a coastal video wall"></div>
  </div>
</section>

</body>
</html>
```